New business card design needed for Trucking/Staffing company!

I am looking for a business card design. The business name is Harbor Lane Freightworks, LLC. This company is a staffing company for commercial drivers/truck drivers. Most of our customers are trucking/supply companies. Our colors are blue/black/white/grey. The info I have on my current business cards is
-Spot for a name
-2 lines for an address
-3 lines for Office, cell, and fax
-email
-website(currently on backside of card with logo but can go anywhere)
Updates

Project Deadline Extended
Reason: Open to more designs

Target Market(s)

Trucking companies, building supply companies

Industry/Entity Type

Business

Contact Information for Business Card

Edgy but professional

Font styles to use
Other font styles liked:
• Open to suggestions

Colors
0555a3
000000
ffffff
9d9d9d

Requirements
Must have
• Must have the logo incorporated

```html
<!DOCTYPE html>
<html lang="en">
<head>
<meta charset="utf-8">
<title>Harbor Lane Freightworks – Business Card</title>
<link rel="stylesheet" href="https://fonts.googleapis.com/css2?family=Open+Sans:wght@400;600;700&display=swap">
<style>
  :root {
    --navy: #22319a;
    --blue: #1b4a8a;
    --black: #000000;
    --ink: #1e1e1e;
    --grey: #9d9d9d;
    --paper: #ffffff;
    --backdrop: #e9e9ec;
  }
  * { margin: 0; padding: 0; box-sizing: border-box; }
  html, body {
    width: 1200px; height: 1000px; overflow: hidden;
    background: var(--backdrop);
    font-family: "Open Sans", sans-serif;
    color: var(--ink);
  }
  .card {
    position: absolute; left: 265px; width: 665px; height: 397px;
    background: var(--paper); border-radius: 26px; overflow: hidden;
    box-shadow: 0 4px 14px rgba(0,0,0,.18);
  }
  .card--front { top: 73px; }
  .card--back { top: 533px; display: flex; align-items: center; justify-content: center; }

  .holder { position: absolute; left: 33px; top: 52px; }
  .holder__name { font-size: 21px; font-weight: 700; color: var(--navy); line-height: 1.2; }
  .holder__role { font-size: 16px; margin-top: 2px; }

  .contacts { position: absolute; left: 33px; top: 137px; list-style: none; }
  .contacts li { display: flex; align-items: center; font-size: 16px; height: 24px; }
  .contacts svg { width: 14px; height: 14px; margin-right: 8px; fill: var(--navy); }

  .company { position: absolute; left: 33px; top: 271px; }
  .company__name { font-size: 16px; font-weight: 700; color: var(--navy); margin-bottom: 3px; }
  .company__line { font-size: 16px; line-height: 22px; }

  .wordmark { display: flex; align-items: center; gap: 10px; color: var(--navy); font-weight: 700; white-space: nowrap; }
  .wordmark__square { background: var(--navy); }
  .card--front .wordmark { position: absolute; left: 300px; top: 186px; font-size: 22px; }
  .card--front .wordmark__square { width: 16px; height: 16px; }
  .card--back .wordmark { font-size: 32px; }
  .card--back .wordmark__square { width: 22px; height: 22px; }

  .band { position: absolute; left: 0; bottom: 0; width: 665px; height: 33px; display: block; }
</style>
</head>
<body>
  <section class="card card--front">
    <div class="holder">
      <p class="holder__name">Daniel Whitmore</p>
      <p class="holder__role">Owner / Founder</p>
    </div>

    <ul class="contacts">
      <li><svg viewBox="0 0 14 14"><rect x="3.5" y="0" width="7" height="14" rx="1.5"/></svg>+ 999 999 999</li>
      <li><svg viewBox="0 0 14 14"><path d="M0 5q7-5 14 0v2H10V5H4v2H0z M2 8h10l1 5H1z"/></svg>+ 999 999 999</li>
      <li><svg viewBox="0 0 14 14"><rect x="3" y="0" width="8" height="4"/><rect x="0" y="5" width="14" height="6" rx="1"/><rect x="3" y="10" width="8" height="4"/></svg>+ 999 999 999</li>
      <li><svg viewBox="0 0 14 14"><path d="M0 3h14v8H0z M1 4l6 4 6-4" stroke="#fff" stroke-width="1"/></svg>info@harborlanefreight.com</li>
      <li><svg viewBox="0 0 14 14"><circle cx="7" cy="7" r="6.5"/><path d="M7 1v12M1 7h12" stroke="#fff" stroke-width="1"/></svg>www.harborlanefreight.com</li>
    </ul>

    <div class="company">
      <p class="company__name">Harbor Lane Freightworks, LLC</p>
      <p class="company__line">48 Quayside Road, Eastmere</p>
      <p class="company__line">Kent ME9 4LQ</p>
    </div>

    <div class="wordmark"><span class="wordmark__square"></span>Harbor Lane Freightworks</div>

    <svg class="band" viewBox="0 0 665 33" preserveAspectRatio="none" aria-hidden="true">
      <path d="M0 1H280Q310 1 316 33H0z" fill="var(--blue)"/>
      <path d="M290 0H665V33H322Q316 4 290 0z" fill="var(--black)"/>
    </svg>
  </section>

  <section class="card card--back">
    <div class="wordmark"><span class="wordmark__square"></span>Harbor Lane Freightworks</div>
  </section>
</body>
</html>
```